Professional and creative business card design for recruiting service providers

Our company supports German medium-sized companies in filling vacancies promptly. For this we use social media marketing and bring our customers into the visibility.

We want a professional but also creative design for our business cards.

Please look at halvenrick-consult.de to get an impression of our CI.

Target Market(s)

Small and medium-sized companies in Germany from the industry

Industry/Entity Type

Industrie, Handwerk

Contact Information for Business Card

Name, Position, Telefonnummer, Email, Website

Colors
EE7325
F08F49
F5BC92
FAE3D3
FDF4ED

Requirements
Must have
• A picture of the employee and in the style of www.halvenrick-consult.de

```html
<!DOCTYPE html>
<html lang="de">
<head>
<meta charset="utf-8">
<title>Halvenrick Consult – Visitenkarte</title>
<link rel="stylesheet" href="https://fonts.googleapis.com/css2?family=Jost:wght@600&family=Arimo:wght@400&display=swap">
<style>
  :root {
    --orange: #ee7325;
    --orange-soft: #f08f49;
    --peach: #f5bc92;
    --blush: #fae3d3;
    --cream: #fdf4ed;
    --ink: #0a0a0a;
    --white: #ffffff;
    --page: #e7e4e1;
  }
  html, body {
    margin: 0;
    width: 1200px;
    height: 900px;
    overflow: hidden;
    background: var(--page);
  }
  .business-card {
    position: absolute;
    left: 100px;
    top: 141px;
    width: 1000px;
    height: 618px;
    overflow: hidden;
    background: linear-gradient(160deg, #f3ecea 0%, #fbf9f8 45%, var(--cream) 100%);
    box-shadow: 0 18px 40px rgba(0, 0, 0, 0.18);
  }
  .brand {
    position: absolute;
    left: 59px;
    top: 118px;
    display: flex;
    align-items: center;
    gap: 28px;
  }
  .brand-mark {
    width: 84px;
    height: 84px;
    background: var(--orange);
  }
  .brand-name {
    font-family: "Jost", sans-serif;
    font-weight: 600;
    font-size: 48px;
    line-height: 50px;
    letter-spacing: 2px;
    color: var(--ink);
    text-transform: uppercase;
  }
  .accent-rule {
    position: absolute;
    left: 0;
    top: 330px;
    width: 602px;
    height: 7px;
    background: var(--orange);
  }
  .contact-band {
    position: absolute;
    left: 0;
    top: 337px;
    width: 1000px;
    height: 281px;
    background: var(--ink);
  }
  .employee-photo {
    position: absolute;
    left: 520px;
    top: 51px;
    width: 470px;
    height: 567px;
    background: linear-gradient(180deg, #c9a28a 0%, #a27a64 32%, #2a2a2e 58%, #1b1b1e 100%);
    border-radius: 200px 200px 0 0;
  }
  .person {
    position: absolute;
    left: 59px;
    top: 362px;
  }
  .person-name {
    margin: 0;
    font-family: "Jost", sans-serif;
    font-weight: 600;
    font-size: 44px;
    line-height: 48px;
    letter-spacing: 0.5px;
    color: var(--orange);
    text-transform: uppercase;
  }
  .person-role {
    margin: 0;
    font-family: "Arimo", sans-serif;
    font-size: 28px;
    line-height: 34px;
    color: var(--white);
  }
  .contact-list {
    position: absolute;
    left: 59px;
    top: 463px;
    margin: 0;
    padding: 0;
    list-style: none;
    font-family: "Arimo", sans-serif;
    font-size: 28px;
    line-height: 36.5px;
    color: var(--white);
  }
  .contact-list li {
    display: flex;
    align-items: center;
    gap: 10px;
  }
  .contact-icon {
    width: 27px;
    height: 27px;
    flex: none;
  }
</style>
</head>
<body>
  <div class="business-card">
    <div class="brand">
      <div class="brand-mark"></div>
      <div class="brand-name">Halvenrick<br>Consult</div>
    </div>

    <div class="accent-rule"></div>
    <div class="contact-band"></div>

    <div class="employee-photo" role="img" aria-label="Portraitfoto des Mitarbeiters in dunklem Sakko und Rollkragenpullover"></div>

    <div class="person">
      <p class="person-name">Lukas Brenner</p>
      <p class="person-role">Managing Director</p>
    </div>

    <ul class="contact-list">
      <li>
        <svg class="contact-icon" viewBox="0 0 24 24" aria-hidden="true">
          <path fill="var(--orange)" d="M6.6 10.8a15.2 15.2 0 0 0 6.6 6.6l2.2-2.2a1 1 0 0 1 1-.25 11.4 11.4 0 0 0 3.6.57 1 1 0 0 1 1 1V20a1 1 0 0 1-1 1A17 17 0 0 1 3 4a1 1 0 0 1 1-1h3.5a1 1 0 0 1 1 1c0 1.25.2 2.45.57 3.57a1 1 0 0 1-.25 1z"/>
          <path fill="none" stroke="var(--orange)" stroke-width="1.8" stroke-linecap="round" d="M14 3.5a7 7 0 0 1 6.5 6.5M14 7a3.5 3.5 0 0 1 3 3"/>
        </svg>
        <span>030-555 014 276</span>
      </li>
      <li>
        <svg class="contact-icon" viewBox="0 0 24 24" aria-hidden="true">
          <rect x="2" y="5" width="20" height="14" fill="var(--orange)"/>
          <path fill="none" stroke="var(--ink)" stroke-width="1.6" d="M2 5l10 8 10-8M2 19l7.5-7M22 19l-7.5-7"/>
        </svg>
        <span>info@halvenrick-consult.de</span>
      </li>
      <li>
        <svg class="contact-icon" viewBox="0 0 24 24" aria-hidden="true">
          <g fill="none" stroke="var(--orange)" stroke-width="1.8">
            <circle cx="12" cy="12" r="10"/>
            <ellipse cx="12" cy="12" rx="4.5" ry="10"/>
            <path d="M2 12h20M4 6.5h16M4 17.5h16"/>
          </g>
        </svg>
        <span>www.halvenrick-consult.de</span>
      </li>
    </ul>
  </div>
</body>
</html>
```